Qorvilo IT Website

We need a logo design for a new company in Jeffersonville, IN (serving predminately the Louisville, KY area). We merged Tarnwell Information Systems (an IT staffing company) and Cobalt Wayfarers (a business intelligence consulting group). Our logo was completed through Brush Market. We are doing a soft launch as we want one web page with just basic information and link that to the existing web pages we have: 1) www.tarnwellinfo.com and 2) www.cobaltwayfarers.com.
The 3 tabs we have in mind are:
Services/News/About Us. Under Services are: IT Staffing, Analytics/BI, Strategic Outsourcing, and CIO Services. Under About Us, we have History, Leadership and Contact Us. No submenu for News.
We also want to have the current companies' sites as clickable links. One should be IT Staffing (directed to www.tarnwellinfo.com) and the other should be Business Intelligence/Data Analytics (directed to www.cobaltwayfarers.com).
Target Market(s)
IT professionals and clients needing IT services
Industry/Entity Type
It Company
Coding
Coded - Design and coding required
Number of Pages Required
4 page
Look and feel

```html
<!DOCTYPE html>
<html lang="en">
<head>
<meta charset="utf-8">
<title>Qorvilo IT</title>
<link rel="stylesheet" href="https://fonts.googleapis.com/css2?family=Raleway:wght@400;500;600;700&family=Open+Sans:wght@400;600&family=Noto+Serif:ital@1&display=swap">
<style>
:root{
  --blue:#2a9ad8;
  --blue-deep:#1a73ad;
  --band:#1f5d9c;
  --ink:#222;
  --text:#555;
  --muted:#888;
  --line:#dcdcdc;
  --panel:#f5f5f5;
  --footer:#1e1e1e;
  --white:#fff;
}
*{box-sizing:border-box;margin:0;padding:0}
html,body{width:1200px;height:2675px;overflow:hidden;background:var(--white)}
body{font-family:"Open Sans",Arial,sans-serif;color:var(--text);position:relative}
.raleway{font-family:"Raleway",Arial,sans-serif}

/* header */
.site-header{height:82px;display:flex;align-items:center;justify-content:space-between;padding:0 50px;position:relative;box-shadow:0 1px 4px rgba(0,0,0,.08);z-index:2;background:var(--white)}
.brand{display:flex;align-items:center;gap:10px;font-family:"Raleway",sans-serif;font-weight:700;font-size:34px;color:var(--blue-deep);letter-spacing:.5px}
.brand-mark{width:34px;height:34px;background:var(--blue-deep)}
.main-nav{display:flex;font-family:"Raleway",sans-serif;font-size:15px;color:var(--ink);font-weight:500}
.main-nav a{color:inherit;text-decoration:none;padding:0 27px;border-left:1px solid var(--line);line-height:30px}
.main-nav a:first-child{border-left:none}
.nav-marker{position:absolute;left:502px;bottom:-2px;width:60px;height:3px;background:var(--blue)}

/* hero */
.hero{height:538px;background:linear-gradient(120deg,#c9c4bd 0%,#e4e0da 45%,#b9c3cc 75%,#efece7 100%)}

/* services */
.services{padding-top:46px;height:1035px;position:absolute;top:620px;left:0;width:1200px;height:497px}
.section-title{text-align:center;font-family:"Raleway",sans-serif;font-weight:700;font-size:35px;color:var(--blue-deep);letter-spacing:.5px;line-height:42px}
.section-sub{text-align:center;font-family:"Raleway",sans-serif;font-weight:600;font-size:23px;color:#666;margin-top:2px}
.service-cards{display:flex;gap:40px;padding:0 48px;margin-top:28px}
.service-card{width:246px;height:310px;border:1px solid var(--line);text-align:center;padding:26px 22px 0;color:var(--text)}
.service-card.is-active{background:var(--blue);border-color:var(--blue);color:var(--white)}
.service-card svg{width:76px;height:76px}
.service-card h3{font-family:"Raleway",sans-serif;font-weight:700;font-size:20px;color:var(--ink);margin:12px 0 10px}
.service-card.is-active h3{color:var(--white)}
.service-card p{font-size:15px;line-height:21px}

/* feature */
.feature{position:absolute;top:1117px;left:0;width:1200px;height:363px;display:flex}
.feature-photo{width:562px;background:linear-gradient(135deg,#5b4a3e,#8a7a66 45%,#3e3a3a)}
.feature-body{flex:1;background:var(--panel);padding:36px 60px 0 22px}
.feature-body h2{font-family:"Raleway",sans-serif;font-weight:700;font-size:34px;color:#333}
.rule{width:86px;height:3px;background:var(--blue-deep);margin:16px 0 16px}
.feature-body p{font-family:"Raleway",sans-serif;font-size:14.5px;line-height:21px;color:#444;margin-bottom:18px}
.btn{display:inline-block;border:2px solid #bbb;padding:10px 30px;font-family:"Raleway",sans-serif;font-size:15px;color:#444;border-radius:2px;margin-top:4px}

/* blog + testimonials */
.updates{position:absolute;top:1572px;left:53px;width:1100px;display:flex;gap:60px}
.updates > div{width:520px}
.col-head{display:flex;align-items:center;gap:18px;font-family:"Raleway",sans-serif;font-weight:700;font-size:20px;color:var(--ink)}
.arrows{display:flex;gap:3px}
.arrows span{width:20px;height:20px;border:1px solid #aaa;border-radius:50%;display:flex;align-items:center;justify-content:center}
.arrows svg{width:8px;height:8px}
.col-head-rule{width:60px;height:2px;background:#999;margin-top:8px}
.post{display:flex;gap:18px;margin-top:30px}
.post-thumb{width:192px;height:144px;background:linear-gradient(160deg,#cfd8df,#4c5560 60%,#e08a2a);position:relative;flex:none}
.post-date{position:absolute;top:12px;left:12px;background:rgba(40,40,40,.8);color:#fff;width:46px;text-align:center;font-size:20px;padding:4px 0}
.post-date small{display:block;font-size:10px;background:var(--blue);margin-top:3px}
.post h4{font-family:"Raleway",sans-serif;font-weight:500;font-size:18px;color:var(--ink);margin-top:0}
.post p{font-size:12px;line-height:19px;color:var(--muted);margin-top:10px}
.post-meta{display:flex;justify-content:space-between;margin-top:30px;font-size:12px;color:var(--muted)}
.post-meta span{display:flex;align-items:center;gap:6px}
.post-meta svg{width:10px;height:10px}
.testimonial{display:flex;gap:10px;margin-top:40px}
.quote-mark{font-family:Georgia,serif;font-size:44px;line-height:30px;color:var(--blue)}
.testimonial p{font-family:"Noto Serif",Georgia,serif;font-style:italic;font-size:12.5px;line-height:20px;color:#777}
.author{display:flex;align-items:center;gap:18px;margin:22px 0 0 36px}
.avatar-sm{width:46px;height:46px;border-radius:50%;background:linear-gradient(#e6cfae,#b08860)}
.author b{display:block;font-family:"Raleway",sans-serif;font-size:12px;font-weight:700;color:#333}
.author i{font-style:normal;font-size:12px;color:var(--muted)}

/* quote band */
.quote-band{position:absolute;top:1885px;left:0;width:1200px;height:430px;background:linear-gradient(160deg,#2a6aa8,var(--band) 55%,#174a80);text-align:center;color:var(--white)}
.avatar-lg{width:82px;height:82px;border-radius:50%;border:3px solid #fff;margin:78px auto 0;background:radial-gradient(circle,#e8cfb4 0 38%,#fff 40%)}
.quote-band p{font-style:italic;font-size:15px;line-height:21px;width:1060px;margin:30px auto 0;text-align:left}
.band-rule{width:180px;height:1px;background:rgba(255,255,255,.7);margin:46px auto 0}
.quote-band h5{font-family:"Raleway",sans-serif;font-weight:700;font-size:19px;margin-top:12px}
.quote-band em{font-size:14px}

/* footer */
.site-footer{position:absolute;top:2315px;left:0;width:1200px;height:308px;background:var(--footer);color:var(--white);display:flex;padding:0 0 0 67px}
.foot-col h6{font-family:"Raleway",sans-serif;font-weight:500;font-size:23px;padding-top:50px;padding-bottom:8px;border-bottom:2px solid #ddd;width:220px}
.foot-col{font-size:14px}
.foot-col.about{width:295px}
.foot-col.svc{width:268px}
.foot-col.news{width:288px}
.foot-brand{display:flex;align-items:center;gap:8px;font-family:"Raleway",sans-serif;font-weight:700;font-size:26px;color:#ccc;margin:20px 0 14px}
.foot-brand i{width:24px;height:24px;background:#ccc}
.foot-col.about p{font-size:14px;line-height:20px;width:225px}
.foot-list{list-style:none;margin:20px 0 0 5px;width:215px}
.foot-list li{padding:6px 0 7px;border-bottom:1px solid #555;font-size:14px}
.foot-list li:last-child{border:none}
.news-list li{padding:6px 0 10px;line-height:19px}
.contact-block{margin:20px 0 0 3px;line-height:21px;font-size:14px}
.bottom-bar{position:absolute;top:2623px;left:0;width:1200px;height:52px;background:var(--blue);color:var(--white);text-align:center;line-height:52px;font-size:14px;font-family:"Raleway",sans-serif}
</style>
</head>
<body>

<header class="site-header">
  <div class="brand"><span class="brand-mark"></span>Qorvilo IT</div>
  <nav class="main-nav">
    <a href="#">HOME</a><a href="#">SERVICES</a><a href="#">NEWS</a><a href="#">ABOUT US</a><a href="#">CONTACT</a>
  </nav>
  <span class="nav-marker"></span>
</header>

<section class="hero" role="img" aria-label="Photo of IT colleagues discussing work at a desktop monitor in a bright office"></section>

<section class="services">
  <h2 class="section-title">WHO YOU ARE</h2>
  <div class="section-sub">Our Services</div>
  <div class="service-cards">
    <article class="service-card is-active">
      <svg viewBox="0 0 76 76"><rect x="8" y="22" width="56" height="40" rx="4" fill="#fff"/><rect x="26" y="12" width="20" height="12" rx="2" fill="none" stroke="#fff" stroke-width="4"/><path d="M55 46 L70 72 L40 72Z" fill="#fff" stroke="#2a9ad8" stroke-width="3"/><rect x="53.5" y="54" width="3" height="10" fill="#2a9ad8"/></svg>
      <h3>IT Staffing</h3>
      <p>Lorem Ipsum is simply dummy text of the printing and typesetting industry. Lorem Ipsum has been the industry's standard dummy text ever since the 1500</p>
    </article>
    <article class="service-card">
      <svg viewBox="0 0 76 76" fill="#333"><circle cx="26" cy="24" r="12"/><circle cx="50" cy="24" r="12"/><path d="M6 66 C6 44 20 38 38 38 C56 38 70 44 70 66Z"/></svg>
      <h3>Analytics/BI</h3>
      <p>Lorem Ipsum is simply dummy text of the printing and typesetting industry. Lorem Ipsum has been the industry's standard dummy text ever since the 1500</p>
    </article>
    <article class="service-card">
      <svg viewBox="0 0 76 76"><ellipse cx="38" cy="34" rx="18" ry="22" fill="#333"/><text x="38" y="42" text-anchor="middle" font-size="22" fill="#fff" font-family="Arial">$</text><path d="M6 48 Q38 80 70 48 L64 48 Q38 70 12 48Z" fill="#333"/></svg>
      <h3>Strategic Outsourcing</h3>
      <p>Lorem Ipsum is simply dummy text of the printing and typesetting industry. Lorem Ipsum has been the industry's standard dummy text ever since the 1500</p>
    </article>
    <article class="service-card">
      <svg viewBox="0 0 76 76" fill="#333"><circle cx="18" cy="30" r="8"/><circle cx="58" cy="30" r="8"/><circle cx="38" cy="24" r="10"/><path d="M4 62 C4 46 10 42 18 42 C26 42 32 46 32 62Z"/><path d="M44 62 C44 46 50 42 58 42 C66 42 72 46 72 62Z"/><path d="M20 64 C20 42 28 37 38 37 C48 37 56 42 56 64Z"/></svg>
      <h3>CIO Services</h3>
      <p>Lorem Ipsum is simply dummy text of the printing and typesetting industry. Lorem Ipsum has been the industry's standard dummy text ever since the 1500</p>
    </article>
  </div>
</section>

<section class="feature">
  <div class="feature-photo" role="img" aria-label="Overhead photo of a team meeting around a round table with papers"></div>
  <div class="feature-body">
    <h2>Moving Things For You</h2>
    <div class="rule"></div>
    <p>Lorem ipsum dolor sit amet, consectetuer adipiscing elit. Aenean commodo ligula eget dolor. Aenean massa. Cum sociis natoque penatibus et magnis dis parturient montes, nascetur ridiculus mus. Donec quam felis, ultricies nec, pellentesque eu, pretium quis, sem.</p>
    <p>Aenean vulputate eleifend tellus. Aenean leo ligula, porttitor eu, consequat vitae, eleifend ac, enim.</p>
    <span class="btn">Learn More</span>
  </div>
</section>

<section class="updates">
  <div class="blog">
    <div class="col-head">LATEST BLOG POSTS
      <span class="arrows"><span><svg viewBox="0 0 8 8"><path d="M5 1 L2 4 L5 7" fill="none" stroke="#777" stroke-width="1.3"/></svg></span><span><svg viewBox="0 0 8 8"><path d="M3 1 L6 4 L3 7" fill="none" stroke="#777" stroke-width="1.3"/></svg></span></span>
    </div>
    <div class="col-head-rule"></div>
    <div class="post">
      <div class="post-thumb" role="img" aria-label="Photo of a businessman holding an umbrella and folders">
        <div class="post-date">06<small>MAY</small></div>
      </div>
      <div>
        <h4>Help your business to success</h4>
        <p>Morbi vehicula a nibh in commodo. Aliquam quis dolor eget lectus pulvinar eu rhoncus ligula. Ut leo mauris, molestie imperdiet consequat in, varius ac sapien.</p>
        <div class="post-meta">
          <span><svg viewBox="0 0 10 10"><path d="M0 0 H5 L10 5 L5 10 L0 5Z" fill="#2a9ad8"/></svg>Development, Maketing</span>
          <span><svg viewBox="0 0 10 10"><rect width="10" height="10" fill="#2a9ad8"/><path d="M5 2 V8 M2 5 H8" stroke="#fff" stroke-width="1.5"/></svg>Read more</span>
        </div>
      </div>
    </div>
  </div>
  <div class="testimonials">
    <div class="col-head">TESTIMONIALS
      <span class="arrows"><span><svg viewBox="0 0 8 8"><path d="M5 1 L2 4 L5 7" fill="none" stroke="#777" stroke-width="1.3"/></svg></span><span><svg viewBox="0 0 8 8"><path d="M3 1 L6 4 L3 7" fill="none" stroke="#777" stroke-width="1.3"/></svg></span></span>
    </div>
    <div class="col-head-rule"></div>
    <div class="testimonial">
      <span class="quote-mark">&ldquo;</span>
      <p>Morbi auctor vel mauris facilisis lacinia. Aenean suscipit lorem leo, et hendrerit odio fermentum et. Donec ac dolor eros. Mauris arcu nunc, iaculis sit amet lacus iaculis, faucibus faucibus nunc. Vestibulum sit amet lacinia massa</p>
    </div>
    <div class="author">
      <span class="avatar-sm" role="img" aria-label="Portrait photo of the client"></span>
      <div><b>DANA WHITLOW</b><i>Maketing Manager</i></div>
    </div>
  </div>
</section>

<section class="quote-band" role="group" aria-label="Partner quote over a blue-tinted office photo">
  <div class="avatar-lg" role="img" aria-label="Portrait photo of the partner"></div>
  <p>Lorem ipsum dolor sit amet, consectetuer adipiscing elit. Aenean commodo ligula eget dolor. Aenean massa. Cum sociis natoque penatibus et magnis dis parturient montes, nascetur ridiculus mus. Donec quam felis, ultricies nec, pellentesque eu, pretium quis, sem.</p>
  <div class="band-rule"></div>
  <h5>Mira Halden</h5>
  <em>Partner</em>
</section>

<footer class="site-footer">
  <div class="foot-col about">
    <h6>WHO WE ARE</h6>
    <div class="foot-brand"><i></i>Qorvilo IT</div>
    <p>Lorem ipsum dolor sit amet, consectetur adipisicing elit, sed do eiusmod tempor incididunt ut labore et dolore magnat, consectetur adipisicing elit.</p>
  </div>
  <div class="foot-col svc">
    <h6>OUR SERVICES</h6>
    <ul class="foot-list">
      <li>Business Intelligence</li><li>Data Warehousing</li><li>Data Integration</li><li>BI Operations Reporting</li><li>Data Quality</li>
    </ul>
  </div>
  <div class="foot-col news">
    <h6>RECENT NEWS</h6>
    <ul class="foot-list news-list">
      <li>Front-end processes with effective<br>3 days ago</li>
      <li>User friendly intellectual capital<br>5 days ago</li>
      <li>Innovate open-source infrastructures<br>1 month ago</li>
    </ul>
  </div>
  <div class="foot-col contact">
    <h6>CONTACT</h6>
    <div class="contact-block">London<br>Harbor Lane Partners<br>3rd Floor 22 Fernmoor Street<br>London<br>W4 2QT<br>United Kingdom<br>T +44 (0)203 555 0148</div>
  </div>
</footer>
<div class="bottom-bar">&copy; 2016 Copyright Qorvilo | All rights reserved | Privacy Policy</div>

</body>
</html>
```